Brightfield Co Trade Show Flyer

We need a brochure design (8.5 x 11) Info in the design (refer to rough draft I drew on Paper): "#1 selling tool to aquire new franchisees has been video testimonials" - Martin L. Crowe, C.E.O Tovik Smoothie Franchise Testimonials - Let your franchisees do the selling for you. Franchisee testimonial: $10,000 / per Franchisee Includes: • 2 minute Video • 1 minute add for your franchise's location • Concept creation • Communication with franchisee • Travel to their location • All rental equipment • 1 round of corrections • Animated logo • Licensed music ******* For 25% Discount section (next to middle box), please put the "Outlet Summit Logo" Great to use on all your social media (USE logos and icons) • Website • Vidstream • Workly • Pagely • Snapora • Chirpa • Phone calls • Emails • In person meetings Some of our clients: (use the logos I uploaded - in round boxes as in draft) LOGO (Brightfield Franchise Testimonial) www.brightfieldvoices.example (866) 555-0172

Target Market(s)

Franchise owners

Colors

Designer to choose colors to be used in the design.

Requirements

```html
<!DOCTYPE html>
<html lang="en">
<head>
<meta charset="utf-8">
<title>Brightfield Co – Franchise Testimonials</title>
<link rel="stylesheet" href="https://fonts.googleapis.com/css2?family=Archivo+Black&family=Montserrat:wght@700;900&family=Signika:wght@300;400;600&display=swap">
<style>
  :root {
    --navy: #232c4f;
    --navy-mid: #2c3766;
    --navy-line: #2b3358;
    --teal: #00a98f;
    --teal-dark: #1f6f66;
    --white: #ffffff;
    --ink: #111111;
    --chip: #3a4a86;
  }
  * { margin: 0; padding: 0; box-sizing: border-box; }
  html, body { width: 927px; height: 1200px; overflow: hidden; background: var(--white); }
  .flyer { position: relative; width: 927px; height: 1200px; overflow: hidden; background: var(--white); font-family: "Signika", sans-serif; color: var(--white); }
  .backdrop { position: absolute; inset: 0; }
  .frame { position: absolute; left: 13px; right: 13px; top: 900px; bottom: 10px; border: 1.5px solid var(--navy-line); border-top: none; }
  .abs { position: absolute; }
  .quote { left: 0; width: 927px; top: 22px; text-align: center; font-size: 27px; font-weight: 400; letter-spacing: 0.1px; }
  .attribution { right: 37px; top: 54px; text-align: right; font-family: Arial, sans-serif; font-size: 18px; line-height: 22px; }
  .title-top { left: 46px; width: 836px; top: 118px; display: flex; justify-content: space-between; font-family: "Archivo Black", sans-serif; font-size: 92px; line-height: 100px; }
  .title-rule { left: 48px; width: 831px; top: 209px; height: 3px; background: var(--white); }
  .title-main { left: 44px; width: 840px; top: 212px; text-align: center; font-family: "Archivo Black", sans-serif; font-size: 97px; line-height: 100px; letter-spacing: -1px; }
  .tagline { left: 0; width: 927px; top: 306px; text-align: center; font-size: 35px; font-weight: 300; }
  .burst { left: 14px; top: 352px; width: 334px; height: 334px; }
  .burst-text { left: 45px; top: 408px; width: 272px; text-align: center; font-family: "Montserrat", sans-serif; font-weight: 900; }
  .burst-percent { font-size: 56px; line-height: 56px; }
  .burst-discount { font-size: 37px; line-height: 40px; }
  .burst-for { font-size: 24px; line-height: 26px; }
  .burst-event { font-family: "Signika", sans-serif; font-weight: 600; font-size: 21px; line-height: 21px; text-align: left; margin: 2px 0 0 70px; }
  .burst-strip { display: inline-block; margin-top: 8px; background: #b7e8df; color: var(--teal); font-size: 7.5px; letter-spacing: 0.6px; padding: 1px 8px; width: 140px; }
  .includes { left: 362px; top: 374px; list-style: none; font-size: 27px; font-weight: 300; line-height: 33px; }
  .includes li::before { content: "·"; display: inline-block; width: 16px; font-weight: 600; }
  .everywhere { left: 0; width: 927px; top: 696px; text-align: center; font-size: 45px; font-weight: 300; }
  .channels { left: 151px; top: 764px; display: flex; gap: 41px; }
  .channel { width: 54px; height: 54px; border-radius: 50%; background: var(--chip); display: flex; align-items: center; justify-content: center; font-size: 10px; font-weight: 600; color: var(--white); }
  .channel.phone { background: #1b84bf; }
  .divider { left: 175px; width: 577px; top: 835px; height: 2px; background: var(--white); border-radius: 1px; }
  .trusted { left: 0; width: 927px; top: 849px; text-align: center; font-size: 31px; font-weight: 300; }
  .clients { left: 196px; top: 901px; display: flex; gap: 29px; }
  .client { width: 84px; height: 84px; border-radius: 50%; background: var(--white); display: flex; align-items: center; justify-content: center; text-align: center; color: var(--navy); font-size: 12px; font-weight: 600; line-height: 13px; padding: 6px; }
  .brand-mark { left: 437px; top: 1022px; width: 54px; height: 54px; border-radius: 50%; background: var(--ink); }
  .brand-name { left: 0; width: 927px; top: 1096px; text-align: center; font-family: "Archivo Black", sans-serif; font-size: 40px; line-height: 44px; color: var(--ink); }
  .brand-sub { left: 0; width: 927px; top: 1140px; text-align: center; font-family: "Montserrat", sans-serif; font-weight: 700; font-size: 11px; color: var(--ink); }
  .contact { left: 0; width: 927px; top: 1158px; text-align: center; font-family: "Montserrat", sans-serif; font-weight: 700; font-size: 22px; color: #222; }
</style>
</head>
<body>
<main class="flyer">
  <svg class="backdrop" width="927" height="1200" viewBox="0 0 927 1200" aria-hidden="true">
    <defs>
      <radialGradient id="navyGlow" cx="0.5" cy="0.55" r="0.6">
        <stop offset="0" stop-color="#2e3a6c"/>
        <stop offset="1" stop-color="#222b4c"/>
      </radialGradient>
    </defs>
    <path d="M0 0 H927 V928 Q463 1075 0 928 Z" fill="url(#navyGlow)"/>
  </svg>
  <div class="frame"></div>

  <p class="abs quote">“#1 selling tool to aquire new franchisees has been video testimonials"</p>
  <p class="abs attribution">-Martin L. Crowe,<br>C.E.O Tovik Smoothie</p>

  <h1>
    <span class="abs title-top"><span>F</span><span>R</span><span>A</span><span>N</span><span>C</span><span>H</span><span>I</span><span>S</span><span>E</span></span>
    <span class="abs title-rule"></span>
    <span class="abs title-main">TESTIMONIALS</span>
  </h1>
  <p class="abs tagline">‘Let your franchisees do the selling for you’</p>

  <svg class="abs burst" viewBox="-167 -167 334 334" aria-hidden="true">
    <polygon transform="scale(1.06)" fill="none" stroke="var(--teal)" stroke-width="2"
      points="158,0 120,24 146,60 101,68 112,112 68,101 60,146 24,120 0,158 -24,120 -60,146 -68,101 -112,112 -101,68 -146,60 -120,24 -158,0 -120,-24 -146,-60 -101,-68 -112,-112 -68,-101 -60,-146 -24,-120 0,-158 24,-120 60,-146 68,-101 112,-112 101,-68 146,-60 120,-24"/>
    <polygon fill="var(--teal)" stroke="var(--teal-dark)" stroke-width="4"
      points="158,0 120,24 146,60 101,68 112,112 68,101 60,146 24,120 0,158 -24,120 -60,146 -68,101 -112,112 -101,68 -146,60 -120,24 -158,0 -120,-24 -146,-60 -101,-68 -112,-112 -68,-101 -60,-146 -24,-120 0,-158 24,-120 60,-146 68,-101 112,-112 101,-68 146,-60 120,-24"/>
  </svg>
  <div class="abs burst-text">
    <div class="burst-percent">25%</div>
    <div class="burst-discount">DISCOUNT</div>
    <div class="burst-for">FOR</div>
    <div class="burst-event">The<br>Outlet<br>Summit</div>
    <div class="burst-strip">OWN YOUR OWN BUSINESS!</div>
  </div>

  <ul class="abs includes">
    <li>2 minute Video</li>
    <li>1 minute add for your franchise's location</li>
    <li>Concept creation</li>
    <li>Communication with franchisee</li>
    <li>Travel to their location</li>
    <li>All rental equipment</li>
    <li>1 round of corrections</li>
    <li>Animated logo</li>
    <li>Licensed music</li>
  </ul>

  <h2 class="abs everywhere">Use your Testimonials Everywhere</h2>
  <div class="abs channels">
    <span class="channel">Pagely</span>
    <span class="channel">Snapora</span>
    <span class="channel">Chirpa</span>
    <span class="channel">Vidstream</span>
    <span class="channel">Workly</span>
    <span class="channel">Mailo</span>
    <span class="channel phone" aria-label="Phone">
      <svg width="26" height="26" viewBox="0 0 24 24" aria-hidden="true"><path fill="#fff" d="M6.6 10.8a15 15 0 0 0 6.6 6.6l2.2-2.2a1 1 0 0 1 1-.25 11.4 11.4 0 0 0 3.6.57 1 1 0 0 1 1 1V20a1 1 0 0 1-1 1A17 17 0 0 1 3 4a1 1 0 0 1 1-1h3.5a1 1 0 0 1 1 1c0 1.25.2 2.45.57 3.57a1 1 0 0 1-.25 1z"/></svg>
    </span>
  </div>
  <div class="abs divider"></div>

  <h3 class="abs trusted">Trusted by:</h3>
  <div class="abs clients">
    <span class="client">Cleanstar Systems</span>
    <span class="client">Axleway Care</span>
    <span class="client">Scoopwell</span>
    <span class="client">Cornerday</span>
    <span class="client">Tovik Smoothie</span>
  </div>

  <span class="abs brand-mark" aria-hidden="true"></span>
  <p class="abs brand-name">BRIGHTFIELD</p>
  <p class="abs brand-sub">— FRANCHISE TESTIMONIALS —</p>
  <p class="abs contact">www.brightfieldvoices.example | (866) 555-0172</p>
</main>
</body>
</html>
```